Velmora Junior Reading & Counting Drive

Development of the (VJRCD) website. The Velmora Junior Reading and Counting Drive (VJRCD) is a Velmora Office of Schooling Project running in approximately 810 participating Gauteng Primary Schools. The project goals are to improve Language and Mathematics scores in participating schools.
The colors should be the same colors as Velmora Schooling office colors ( see logos)

Try bring in human element - this project is about improving literacy and numeracy levels of marginalized primary school children.

Target Market(s)

Education sector and general public

Industry/Entity Type

School

Requirements
Must have
• The primary navigation of the site must always be displayed on each page.
? Each section must have a main page where visitors can navigate to the sub items under the relevant section.
? The overall design concept for the website must be optimised in terms of brand identity, accessibility, usability and content distribution. Colours and images must be chosen according to VJRCD’s corporate identity requirements.
? The VJRCD’s logo should be present on the homepage and visible at all times during a person’s visit.

```html
<!DOCTYPE html>
<html lang="en">
<head>
<meta charset="utf-8">
<title>VJRCD – Velmora Junior Reading &amp; Counting Drive</title>
<link rel="stylesheet" href="https://fonts.googleapis.com/css2?family=Source+Sans+3:wght@400;600&display=swap">
<style>
:root{
  --blue:#0054a6;
  --blue-dark:#00447f;
  --ink:#333;
  --ink-soft:#555;
  --page:#f5f5f5;
  --band:#e4e4e4;
  --panel:#e9e9e9;
  --footer:#2b2b2b;
  --rule:#bdbdbd;
  --sand:#e9d7bb;
  --earth:#8a5a3a;
}
*{box-sizing:border-box;margin:0;padding:0}
html,body{width:1200px;height:1200px;overflow:hidden;background:var(--page)}
body{font-family:"Source Sans 3",Arial,sans-serif;color:var(--ink)}
.stage{width:1100px;height:1100px;transform:scale(1.0909);transform-origin:0 0;position:relative}
.abs{position:absolute}

.site-header{left:62px;top:4px;width:975px;height:104px;background:linear-gradient(#f7f7f7,#fff 40%);border:1px solid #e2e2e2}
.brand{left:16px;top:18px;display:flex;align-items:center;gap:14px}
.brand-mark{width:62px;height:62px;border-radius:50%;background:var(--blue)}
.brand-name{font-size:21px;font-weight:600;color:var(--blue);line-height:1.1;width:190px}
.contact{right:20px;top:14px;font-size:20px;color:var(--ink);display:flex;align-items:center;gap:10px}
.contact a{color:var(--blue);text-decoration:none}
.top-nav{right:22px;top:62px;display:flex;align-items:center;font-size:14px;color:var(--ink)}
.top-nav span.sep{margin:0 18px}
.top-nav .active{background:var(--blue);color:#fff;padding:5px 12px;border-radius:3px;border:1px solid var(--blue-dark)}

.section-nav{left:62px;top:108px;width:975px;height:50px;background:var(--band);display:flex;justify-content:center;align-items:center;font-size:13px;letter-spacing:.2px}
.section-nav .sep{margin:0 19px}
.section-nav .current{position:relative;border-bottom:2px solid #888;padding-bottom:1px}
.section-nav .current::after{content:"";position:absolute;left:45px;top:19px;border:6px solid transparent;border-top-color:#888}

.hero-band{left:0;top:158px;width:1100px;height:322px;background:var(--blue)}
.hero{left:62px;top:160px;width:975px;height:318px;background:linear-gradient(90deg,var(--earth) 0%,#c7a27d 35%,var(--sand) 58%,#efe0c6 100%)}
.hero-text{left:551px;top:88px;width:366px;font-size:15.5px;line-height:24px;text-align:justify;color:#3a3a3a}
.dots{left:690px;top:271px;display:flex;gap:14px}
.dots i{width:9px;height:9px;border-radius:50%;background:#444;display:block}
.dots i.on{background:var(--blue)}

.updates{left:62px;top:480px;width:975px;height:205px;background:linear-gradient(90deg,#e3e3e3,#f0f0f0 40%,#e3e3e3);border-bottom:1px solid #d0d0d0;display:flex}
.update{width:325px;padding:28px 22px 0 22px;border-right:1px solid #d4d4d4;margin:22px 0 18px}
.update{margin:0;padding-top:30px}
.update:last-child{border-right:none}
.update-head{display:flex;justify-content:space-between;align-items:baseline;border-bottom:1px solid #aaa;padding-bottom:10px}
.update-head h2{font-size:18px;font-weight:400;color:#333}
.update-head a{font-size:11.5px;color:#555;text-decoration:none}
.update p{font-size:11.5px;line-height:18px;text-align:justify;margin-top:13px}
.meta{font-size:11.5px;font-style:italic;margin-top:8px;display:flex;gap:11px;padding-left:2px}

.goals{left:85px;top:712px;width:240px}
h3.title{font-size:18px;font-weight:400;color:var(--blue)}
.goals h3{border-bottom:1px solid #999;padding-bottom:8px}
.goal{padding:9px 0 8px;border-bottom:2px dotted #aaa}
.goal:last-child{border-bottom:none}
.goal h4{font-size:12.5px;font-weight:400;color:var(--blue)}
.goal p{font-size:11.5px;line-height:16px;text-align:justify;color:var(--ink-soft);margin-top:3px}

.welcome{left:368px;top:712px;width:458px}
.welcome p{font-size:11.5px;line-height:20px;text-align:justify;color:var(--ink-soft);margin-top:18px}
.drive-mark{left:850px;top:720px;width:172px;height:160px;display:flex;flex-direction:column;align-items:center;justify-content:center;gap:12px}
.drive-mark .dot{width:70px;height:70px;border-radius:50%;background:#2c3f86}
.drive-mark span{font-size:26px;font-weight:600;color:#2c3f86}
.photo{left:368px;top:902px;width:200px;height:98px;background:linear-gradient(90deg,#6a8db5,#d9c6a2 55%,#efe8da);border:1px solid #999}
.welcome-more{left:581px;top:902px;width:442px;font-size:11.5px;line-height:20px;text-align:justify;color:var(--ink-soft)}

.site-footer{left:62px;top:1030px;width:975px;height:70px;background:linear-gradient(var(--footer),#1e1e1e);color:#ddd;font-size:12px}
.site-footer .copy{position:absolute;left:24px;top:30px}
.social{position:absolute;right:16px;top:24px;display:flex;gap:7px}
.social i{width:27px;height:27px;border-radius:50%;background:#fff;display:block}
</style>
</head>
<body>
<div class="stage">
  <header class="site-header abs">
    <div class="brand abs"><div class="brand-mark"></div><div class="brand-name">Velmora Office of Schooling</div></div>
    <div class="contact abs">
      <svg width="22" height="18" viewBox="0 0 22 18"><rect x="1" y="4" width="20" height="13" fill="#3a7cc4"/><path d="M1 4l10 7 10-7" fill="none" stroke="#fff" stroke-width="1.2"/><path d="M5 4V1h12v3" fill="#f2c04a"/></svg>
      <span>E - mail : <a href="#">info@vjrcd.org</a></span>
    </div>
    <nav class="top-nav abs">
      <span class="active">Home</span><span class="sep">|</span>
      <span>About the VJRCD</span><span class="sep">|</span>
      <span>Management Team</span><span class="sep">|</span>
      <span>Contact the VJRCD</span>
    </nav>
  </header>

  <nav class="section-nav abs">
    <span class="current">LATEST PROJECTS</span><span class="sep">|</span>
    <span>LATEST NEWS</span><span class="sep">|</span>
    <span>STRUCTURE</span><span class="sep">|</span>
    <span>GOALS</span><span class="sep">|</span>
    <span>CONSULTANTS</span><span class="sep">|</span>
    <span>SERVICE PROVIDERS</span><span class="sep">|</span>
    <span>DISTRICT INVOLMENT</span>
  </nav>

  <div class="hero-band abs"></div>
  <section class="hero abs" role="img" aria-label="Primary school children at their classroom desks, one giving a thumbs up">
    <p class="hero-text abs">Sed ut perspiciatis unde omnis iste natus error sit voluptatem accusantium doloremque laudantium, totam rem aperiam, eaque ipsa quae ab illo inventore veritatis et quasi</p>
    <div class="dots abs"><i></i><i class="on"></i><i></i><i></i><i></i></div>
  </section>

  <section class="updates abs">
    <article class="update">
      <div class="update-head"><h2>LATEST NEWS</h2><a href="#">View all</a></div>
      <p>Sed ut perspiciatis unde omnis iste natus error sit voluptatem accusantium doloremque laudantium, totam rem aperiam, eaque ipsa quae ab illo inventore veritatis et quasi</p>
      <div class="meta"><span>April 12, 2012</span><span>10.30 am</span><span>architecto beatae</span></div>
    </article>
    <article class="update">
      <div class="update-head"><h2>LATEST PROJECTS</h2><a href="#">View all</a></div>
      <p>Sed ut perspiciatis unde omnis iste natus error sit voluptatem accusantium doloremque laudantium, totam rem aperiam, eaque ipsa quae ab illo inventore veritatis et quasi</p>
      <div class="meta"><span>April 12, 2012</span><span>10.30 am</span><span>architecto beatae</span></div>
    </article>
    <article class="update">
      <div class="update-head"><h2>DISTRICT INVOLVEMENTS</h2><a href="#">View all</a></div>
      <p>Sed ut perspiciatis unde omnis iste natus error sit voluptatem accusantium doloremque laudantium, totam rem aperiam, eaque ipsa quae ab illo inventore veritatis et quasi</p>
      <div class="meta"><span>April 12, 2012</span><span>10.30 am</span><span>architecto beatae</span></div>
    </article>
  </section>

  <aside class="goals abs">
    <h3 class="title">OUR GOALS</h3>
    <div class="goal"><h4>Ut enim ad minima veniam</h4><p>Auis nostrum exercitationem ullam corporis suscipit laboriosam, nisi ut aliquid ex ea commodi consequatur.</p></div>
    <div class="goal"><h4>Ut enim ad minima veniam</h4><p>Auis nostrum exercitationem ullam corporis suscipit laboriosam, nisi ut aliquid ex ea commodi consequatur.</p></div>
    <div class="goal"><h4>Ut enim ad minima veniam</h4><p>Auis nostrum exercitationem ullam corporis suscipit laboriosam, nisi ut aliquid ex ea commodi consequatur.</p></div>
  </aside>

  <section class="welcome abs">
    <h3 class="title">WELCOME TO OUR SITE</h3>
    <p>Sed ut perspiciatis unde omnis iste natus error sit voluptatem accusantium doloremque laudantium, totam rem aperiam, eaque ipsa quae ab illo inventore veritatis et quasi architecto beatae vitae dicta sunt explicabo. Nemo enim ipsam voluptatem quia voluptas sit aspernatur aut odit aut fugit, sed quia consequuntur magni dolores eos qui ratione voluptatem sequi nesciunt. Neque porro quisquam est, qui dolorem ipsum quia dolor sit amet, consectetur, adipisci velit, sed quia non numquam eius modi tempora incidunt ut labore et dolore magnam aliquam quaerat voluptatem.</p>
  </section>
  <div class="drive-mark abs"><div class="dot"></div><span>VJRCD</span></div>
  <div class="photo abs" role="img" aria-label="A young pupil writing at a desk"></div>
  <p class="welcome-more abs">Nemo enim ipsam voluptatem quia voluptas sit aspernatur aut odit aut fugit, sed quia consequuntur magni dolores eos qui ratione voluptatem sequi nesciunt. Neque porro quisquam est, qui dolorem ipsum quia dolor sit amet, consectetur, adipisci velit, sed quia non numquam eius modi tempora incidunt ut labore et dolore magnam aliquam quaerat voluptatem.</p>

  <footer class="site-footer abs">
    <span class="copy">Copyright © 2012 www.vjrcd.org &nbsp;&nbsp;All rights reserved</span>
    <div class="social"><i></i><i></i><i></i></div>
  </footer>
</div>
</body>
</html>
```